Feral Tundra, a 3d voxel survival video game needs a card for gaming conventions

I am the lead developer for Feral Tundra http://www.FeralTundra.example and need a business card to hand out at an indie gaming convention
The card would need to include the game name, website url, my name, position (Lead Developer), e-mail and phone number
The game is a 3d, voxel (with smooth terrain) based survival game with guns and wildlife. The main icon of the game would likely be a grizzly bear but I am willing to accept other designs too.
Attached is a media kit for the game with some images you can use but don't have to its just what little art I can provide. Anything on the website or from the video game can also be used. unrelated art can also be used.
Target Market(s)
Indie Developers/publishers at conferences
Industry/Entity Type
Games
Contact Information for Business Card
Name: Corin Wexford
Position: Lead Developer
E-mail: Gray_Lanterns@mailnest.example
Phone number: 555-372-9186
Look and feel

```html
<!DOCTYPE html>
<html lang="en">
<head>
<meta charset="utf-8">
<title>Feral Tundra – Business Card</title>
<link rel="stylesheet" href="https://fonts.googleapis.com/css2?family=Rajdhani:wght@600;700&family=Roboto:wght@400&display=swap">
<style>
  :root {
    --backdrop: #a8a5a5;
    --card: #1f1f21;
    --card-edge: #262628;
    --tan: #b3a57a;
    --band-tan: #878168;
    --red: #9b1a17;
    --white: #f2f2f2;
    --muted: #e0e0e0;
    --rule: #d8d8d8;
    --fur-light: #9a6a45;
    --fur-dark: #4a2e1c;
  }
  html, body {
    margin: 0;
    padding: 0;
    width: 1200px;
    height: 1200px;
    overflow: hidden;
    background: var(--backdrop);
  }
  .canvas {
    position: relative;
    width: 1200px;
    height: 1200px;
  }
  .card {
    position: absolute;
    background: var(--card);
    overflow: hidden;
  }
  .card-front { left: 237px; top: 118px; width: 715px; height: 420px; }
  .card-back  { left: 229px; top: 643px; width: 714px; height: 422px; }

  .photo-roaring-bear {
    position: absolute;
    left: 218px; top: 78px;
    width: 190px; height: 170px;
    border-radius: 45% 45% 10% 10%;
    background: radial-gradient(ellipse at 50% 40%, var(--fur-light), var(--fur-dark) 70%, var(--card) 100%);
  }
  .front-name {
    position: absolute;
    left: 0; right: 0;
    top: 248px;
    text-align: center;
    font-family: "Rajdhani", sans-serif;
    font-weight: 700;
    font-size: 64px;
    line-height: 1;
    letter-spacing: 4px;
    color: var(--tan);
  }

  .photo-standing-bear {
    position: absolute;
    left: 2px; top: 36px;
    width: 178px; height: 222px;
    border-radius: 40% 40% 8% 8%;
    background: linear-gradient(180deg, #b58d66 0%, #8d6240 60%, #3a3533 100%);
  }
  .back-name {
    position: absolute;
    right: 50px; top: 50px;
    font-family: "Rajdhani", sans-serif;
    font-weight: 700;
    font-size: 40px;
    line-height: 1;
    letter-spacing: 3px;
    color: var(--tan);
  }
  .person {
    position: absolute;
    right: 40px; top: 212px;
    text-align: right;
  }
  .person-name {
    font-family: "Rajdhani", sans-serif;
    font-weight: 600;
    font-size: 28px;
    color: var(--white);
    line-height: 1.1;
  }
  .person-role {
    font-family: "Roboto", sans-serif;
    font-size: 16px;
    color: var(--muted);
    margin-top: 4px;
  }
  .rule {
    position: absolute;
    left: 36px; top: 263px;
    width: 486px; height: 1.5px;
    background: var(--rule);
  }
  .contacts {
    position: absolute;
    left: 36px; top: 292px;
    margin: 0; padding: 0;
    list-style: none;
    font-family: "Roboto", sans-serif;
    font-size: 18px;
    color: var(--white);
  }
  .contacts li {
    display: flex;
    align-items: center;
    height: 25px;
  }
  .contacts svg {
    width: 16px; height: 16px;
    margin-right: 19px;
    fill: var(--white);
  }
  .bands { position: absolute; left: 0; bottom: 0; width: 714px; height: 42px; }
</style>
</head>
<body>
<div class="canvas">

  <section class="card card-front">
    <div class="photo-roaring-bear" role="img" aria-label="Photo of a roaring grizzly bear"></div>
    <div class="front-name">FERAL TUNDRA</div>
  </section>

  <section class="card card-back">
    <div class="photo-standing-bear" role="img" aria-label="Photo of a grizzly bear standing on a rock"></div>
    <div class="back-name">FERAL TUNDRA</div>

    <div class="person">
      <div class="person-name">Corin Wexford</div>
      <div class="person-role">Lead Developer</div>
    </div>
    <div class="rule"></div>

    <ul class="contacts">
      <li>
        <svg viewBox="0 0 16 16" aria-hidden="true"><path d="M2 5c0-2 2-3 6-3s6 1 6 3v1h-3V5H5v1H2zM4 7h8l2 7H2z"/></svg>
        555-372-9186
      </li>
      <li>
        <svg viewBox="0 0 16 16" aria-hidden="true"><path d="M8 1a7 7 0 1 0 0 14A7 7 0 0 0 8 1zm0 1.5c.8 0 1.7 1.5 2 4H6c.3-2.5 1.2-4 2-4zM2.6 6.5h2c-.1.9-.1 2.1 0 3h-2a5.5 5.5 0 0 1 0-3zm3.4 3c-.1-.9-.1-2.1 0-3h4c.1.9.1 2.1 0 3zm5.4 0c.1-.9.1-2.1 0-3h2a5.5 5.5 0 0 1 0 3zM8 13.5c-.8 0-1.7-1.5-2-4h4c-.3 2.5-1.2 4-2 4z"/></svg>
        www.feraltundra.example
      </li>
      <li>
        <svg viewBox="0 0 16 16" aria-hidden="true"><path d="M1 3h14v1L8 9 1 4zm0 3 7 5 7-5v7H1z"/></svg>
        Gray_Lanterns@mailnest.example
      </li>
    </ul>

    <svg class="bands" viewBox="0 0 714 42" aria-hidden="true">
      <rect x="0" y="22" width="395" height="20" fill="var(--band-tan)"/>
      <polygon points="400,0 714,0 714,42 378,42" fill="var(--red)"/>
    </svg>
  </section>

</div>
</body>
</html>
```